Innovative Bitcoin Powerpoint Presentation

I have constructred most of the data for a 15 page powerpoint presentation on an innovative bitcoin idea that provides access to fiat currency with bitcoin hodlings

I need this to look great as a first blush to potential investors

Reason: updated deck and name

Target Market(s)

Venture Capital firms and private equity firms

Requirements
Must have
• Fun, innovateive deck, very clean
Should not have
• any generic feel - no templates

```html
<!DOCTYPE html>
<html lang="en">
<head>
<meta charset="utf-8">
<title>Tallyfold – Investor Deck</title>
<link rel="stylesheet" href="https://fonts.googleapis.com/css2?family=Lato:ital,wght@0,400;0,700;1,300&family=Tinos&display=swap">
<style>
  :root{
    --teal:#2fae9a;
    --blue:#2f6eb0;
    --orange:#f5a04e;
    --ink:#1b1b1b;
    --paper:#ffffff;
    --ground:#e9e6e1;
  }
  *{box-sizing:border-box;margin:0;padding:0}
  html,body{width:1200px;height:849px;overflow:hidden;background:var(--ground)}
  .board{position:relative;width:1200px;height:849px}
  .slide{position:absolute;width:354px;height:265px;background:var(--paper);box-shadow:0 2px 6px rgba(0,0,0,.18);font-family:"Tinos",serif;color:var(--ink)}
  .slide__num{position:absolute;left:16px;top:0;width:16px;height:26px;background:var(--ink);color:#fff;font:700 6px "Lato",sans-serif;display:flex;align-items:flex-end;justify-content:center;padding-bottom:4px}
  .slide__title{position:absolute;left:40px;top:28px;font:300 italic 17px "Lato",sans-serif;color:var(--ink)}
  .brand{position:absolute;left:14px;bottom:8px;font:700 9px "Lato",sans-serif;color:var(--orange)}
  .stripe{position:absolute;right:0;bottom:30px;height:6px;width:272px;display:flex}
  .stripe span{flex:1}
  .stripe span:nth-child(1){background:var(--orange)}
  .stripe span:nth-child(2){background:var(--teal)}
  .stripe span:nth-child(3){background:var(--blue)}
  .tile{position:absolute;color:#fff;font:700 8px "Lato",sans-serif;display:flex;align-items:center;justify-content:center;text-align:center;line-height:1.2}
  .op{position:absolute;font:400 18px "Lato",sans-serif;color:var(--ink)}
  .chip{position:absolute;top:174px;height:22px;width:62px;color:#fff;font:400 6.5px "Tinos",serif;display:flex;align-items:center;justify-content:center;text-align:center;line-height:1.1}
  .teal{background:var(--teal)} .blue{background:var(--blue)} .orange{background:var(--orange)}
  .name-box{position:absolute;left:262px;top:75px;width:72px;height:42px;border:1px solid var(--teal);display:flex;align-items:center;justify-content:center;font:700 8px "Lato",sans-serif;color:var(--orange)}
  .bullets{position:absolute;left:78px;top:82px;font-size:7px;line-height:1.45;list-style:none}
  .bullets li.sub{padding-left:18px}
  .pillar{position:absolute;top:70px;width:84px;height:124px;border-radius:10px;color:#fff;font-size:7px;text-align:center}
  .pillar__disc{width:60px;height:60px;border-radius:50%;background:#fff;color:var(--ink);margin:8px auto 0;display:flex;align-items:center;justify-content:center;font-size:7px;line-height:1.2;padding:6px}
  .pillar__text{margin-top:10px;padding:0 6px;line-height:1.3}
  .stat{position:absolute;top:80px;width:64px;text-align:center}
  .stat__disc{width:44px;height:44px;border-radius:50%;margin:0 auto;color:#fff;font-size:8px;display:flex;align-items:center;justify-content:center;text-align:center;line-height:1.1}
  .stat__cap{margin-top:10px;font-size:7px;line-height:1.2}
</style>
</head>
<body>
<main class="board">

  <section class="slide" style="left:68px;top:24px">
    <div class="slide__num">1</div>
    <h2 class="slide__title">Overview</h2>
    <div class="tile teal" style="left:27px;top:75px;width:44px;height:42px">Line of<br>Credit</div>
    <div class="op" style="left:79px;top:84px">+</div>
    <div class="tile blue" style="left:109px;top:75px;width:44px;height:42px">Digital<br>Wallet</div>
    <div class="op" style="left:162px;top:84px">+</div>
    <div class="tile orange" style="left:186px;top:75px;width:38px;height:42px">Debit<br>Card</div>
    <div class="op" style="left:236px;top:84px">=</div>
    <div class="name-box">Tallyfold</div>
    <div class="chip teal" style="left:16px">Scalable technology</div>
    <div class="chip blue" style="left:102px">Lower transaction costs</div>
    <div class="chip orange" style="left:188px">First mover advantage</div>
    <div class="chip teal" style="left:274px">Global Opportunity</div>
    <svg style="position:absolute;left:0;top:178px" width="354" height="14">
      <g fill="var(--ink)">
        <path d="M82 4h10v-3l6 6-6 6v-3H82z"/>
        <path d="M168 4h10v-3l6 6-6 6v-3h-10z"/>
        <path d="M254 4h10v-3l6 6-6 6v-3h-10z"/>
      </g>
    </svg>
    <div class="stripe"><span></span><span></span><span></span></div>
    <div class="brand">Tallyfold</div>
  </section>

  <section class="slide" style="left:764px;top:14px">
    <div class="slide__num">2</div>
    <h2 class="slide__title">Opportunity</h2>
    <ul class="bullets">
      <li>➢&nbsp; Bitcoin rich, cash poor</li>
      <li>➢&nbsp; Selling Bitcoins for cash is expensive</li>
      <li class="sub">• Wide Bid/Ask Spreads</li>
      <li class="sub">• High transaction costs</li>
      <li>➢&nbsp; Significant opportunity cost</li>
      <li class="sub">• Give away upside in BTC price</li>
      <li>➢&nbsp; No operating leverage</li>
      <li class="sub">• Inverse relationship between fiat currency/BTC</li>
    </ul>
    <div class="stripe"><span></span><span></span><span></span></div>
    <div class="brand">Tallyfold</div>
  </section>

  <section class="slide" style="left:422px;top:290px">
    <div class="slide__num">4</div>
    <h2 class="slide__title">Cash vs. Coin Relationship</h2>
    <svg style="position:absolute;left:0;top:0" width="354" height="265" font-family="Lato, sans-serif">
      <text x="90" y="96" font-size="6.5" text-anchor="middle" fill="var(--ink)">Current Relationship</text>
      <text x="245" y="96" font-size="6.5" text-anchor="middle" fill="var(--ink)">Tallyfold</text>
      <rect x="38" y="100" width="104" height="52" rx="10" fill="none" stroke="var(--teal)" stroke-width="5"/>
      <rect x="200" y="100" width="104" height="52" rx="10" fill="none" stroke="var(--orange)" stroke-width="5"/>
      <g role="img" aria-label="Coin and cash icons">
        <circle cx="68" cy="126" r="17" fill="var(--ink)"/>
        <rect x="96" y="110" width="32" height="32" fill="var(--ink)"/>
        <circle cx="228" cy="126" r="17" fill="var(--ink)"/>
        <rect x="256" y="110" width="32" height="32" fill="var(--ink)"/>
      </g>
      <path d="M18 164V96h-5l9-14 9 14h-5v68z" fill="var(--teal)"/>
      <text transform="translate(24 160) rotate(-90)" font-size="5" fill="#fff">Rising BTC value</text>
      <path d="M150 82v68h-5l9 14 9-14h-5V82z" fill="var(--teal)"/>
      <text transform="translate(152 88) rotate(90)" font-size="5" fill="#fff">Shrinking cash</text>
      <path d="M178 164V96h-5l9-14 9 14h-5v68z" fill="var(--orange)"/>
      <text transform="translate(184 162) rotate(-90)" font-size="5" fill="#fff">Greater BTC holdings</text>
      <path d="M318 164V96h-5l9-14 9 14h-5v68z" fill="var(--orange)"/>
      <text transform="translate(324 162) rotate(-90)" font-size="5" fill="#fff">Operating leverage</text>
      <path d="M126 196h96v-6l12 10-12 10v-6h-96z" fill="var(--blue)"/>
      <text x="174" y="202" font-size="6" text-anchor="middle" fill="#fff">Potential Relationship</text>
    </svg>
    <div class="stripe"><span></span><span></span><span></span></div>
    <div class="brand">Tallyfold</div>
  </section>

  <section class="slide" style="left:40px;top:542px">
    <div class="slide__num">3</div>
    <h2 class="slide__title">Solution</h2>
    <div class="pillar teal" style="left:20px">
      <div class="pillar__disc">Secured line of credit</div>
      <p class="pillar__text">Leverages BTC as collateral</p>
    </div>
    <div class="op" style="left:109px;top:112px">+</div>
    <div class="pillar blue" style="left:128px">
      <div class="pillar__disc">Tallyfold Debit Card</div>
      <p class="pillar__text">Global access to local currency</p>
    </div>
    <div class="op" style="left:218px;top:112px">=</div>
    <div class="pillar orange" style="left:236px">
      <div class="pillar__disc">Operating leverage</div>
      <p class="pillar__text">Relationship between BTC and cash</p>
    </div>
    <div class="stripe"><span></span><span></span><span></span></div>
    <div class="brand">Tallyfold</div>
  </section>

  <section class="slide" style="left:782px;top:562px">
    <div class="slide__num">5</div>
    <h2 class="slide__title">Market Size</h2>
    <div class="stat" style="left:70px">
      <div class="stat__disc teal">$9.5b</div>
      <p class="stat__cap">Market Value of BTC</p>
    </div>
    <div class="stat" style="left:144px">
      <div class="stat__disc blue">15<br>million</div>
      <p class="stat__cap">BTC in circulation</p>
    </div>
    <div class="stat" style="left:218px">
      <div class="stat__disc orange">96k</div>
      <p class="stat__cap">Daily BTC Transactions</p>
    </div>
    <div class="stripe"><span></span><span></span><span></span></div>
    <div class="brand">Tallyfold</div>
  </section>

</main>
</body>
</html>
```